3 x 3 metre trade booth design

We need a design for a 3 x 3 metre corner booth for a conference we are attending. There will therefore be 2 x backdrops that we need to have designed. For one of them we want to have our services displayed as an engaging, modern infographic. For the other, we would like to have our brand tagline and our logo, with a cool background which aligns with what we do.
I have attached a picture of what our booth looked like last year- we designed this ourself and we need it to look much more professional, with a different type of infographic for the
Please see attachment with full design brief attached

```html
<!DOCTYPE html>
<html lang="en">
<head>
<meta charset="utf-8">
<title>Novarya – Corner Booth Backdrops</title>
<link href="https://fonts.googleapis.com/css2?family=Montserrat:wght@500;700;800&family=Roboto:wght@400;500;700&display=swap" rel="stylesheet">
<style>
  :root {
    --page: #ffffff;
    --crimson: #b8223f;
    --magenta: #8a2a6e;
    --violet: #7a2a7c;
    --plum-dark: #5a2852;
    --orange: #ef4423;
    --ring-red: #c7243f;
    --white: #ffffff;
    --label-red: #d42a2a;
    --gold: #e9b23a;
  }
  * { margin: 0; padding: 0; box-sizing: border-box; }
  html, body {
    width: 1200px; height: 1056px; overflow: hidden;
    background: var(--page);
  }
  .booth {
    position: absolute; top: 225px; left: 0;
    width: 1200px; height: 606px;
    display: flex; gap: 4px;
  }
  .backdrop { width: 598px; height: 606px; display: block; }
  .headline, .brand-name, .hub-title {
    font-family: "Montserrat", sans-serif; font-weight: 700; fill: var(--white);
  }
  .brand-sub { font-family: "Roboto", sans-serif; font-weight: 500; fill: var(--white); }
  .service-label { font-family: "Roboto", sans-serif; font-weight: 700; fill: var(--label-red); font-size: 10px; letter-spacing: .3px; }
  .service-item { font-family: "Roboto", sans-serif; font-weight: 400; fill: var(--white); font-size: 10px; }
  .label-box { fill: var(--white); }
  .connector { stroke: var(--white); stroke-width: 1.5; fill: none; }
  .node { fill: var(--white); }
</style>
</head>
<body>
<main class="booth">

  <!-- Brand wall -->
  <svg class="backdrop brand-wall" viewBox="0 0 700 710" preserveAspectRatio="none" aria-label="Brand wall with tagline">
    <defs>
      <linearGradient id="brandBg" x1="0" y1="0" x2="1" y2="1">
        <stop offset="0" stop-color="var(--crimson)"/>
        <stop offset=".5" stop-color="var(--violet)"/>
        <stop offset="1" stop-color="var(--magenta)"/>
      </linearGradient>
    </defs>
    <rect width="700" height="710" fill="url(#brandBg)"/>
    <polygon points="670,0 700,0 700,710 290,710" fill="var(--plum-dark)" opacity=".85"/>
    <g class="brand-lockup">
      <rect x="262" y="202" width="50" height="56" fill="none" stroke="var(--gold)" stroke-width="3"/>
      <text class="brand-name" x="332" y="238" font-size="21" letter-spacing="3">NOVARYA</text>
      <text class="brand-sub" x="332" y="255" font-size="8.5" letter-spacing="1.2">VENDORA MASTERY AGENCY</text>
    </g>
    <text class="headline" x="350" y="344" font-size="32" text-anchor="middle" letter-spacing="1">TRANSFORMING BRANDS INTO</text>
    <text class="headline" x="350" y="385" font-size="32" text-anchor="middle" letter-spacing="1">VENDORA SUCCESS STORIES</text>
  </svg>

  <!-- Services infographic wall -->
  <svg class="backdrop services-wall" viewBox="0 0 710 710" preserveAspectRatio="none" aria-label="Services infographic">
    <defs>
      <linearGradient id="servicesBg" x1="0" y1="0" x2="1" y2="1">
        <stop offset="0" stop-color="var(--plum-dark)"/>
        <stop offset=".45" stop-color="var(--magenta)"/>
        <stop offset="1" stop-color="var(--crimson)"/>
      </linearGradient>
    </defs>
    <rect width="710" height="710" fill="url(#servicesBg)"/>
    <polygon points="0,250 430,0 710,0 710,120 0,560" fill="var(--violet)" opacity=".35"/>

    <g class="hub">
      <circle cx="356" cy="273" r="148" fill="none" stroke="var(--white)" stroke-width="2"/>
      <circle cx="356" cy="273" r="143" fill="var(--violet)"/>
      <circle cx="351" cy="273" r="139" fill="var(--ring-red)"/>
      <circle cx="354" cy="273" r="127" fill="var(--orange)"/>
      <text class="hub-title" x="356" y="268" font-size="21" text-anchor="middle" letter-spacing=".5">FULL SERVICE</text>
      <text class="hub-title" x="356" y="294" font-size="21" text-anchor="middle" letter-spacing=".5">MANAGEMENT</text>
    </g>

    <g class="connectors">
      <path class="connector" d="M203 140 L255 165"/>
      <path class="connector" d="M518 145 L465 175"/>
      <path class="connector" d="M193 390 L239 363"/>
      <path class="connector" d="M518 390 L471 363"/>
      <path class="connector" d="M359 420 L359 472"/>
      <circle class="node" cx="255" cy="165" r="6"/>
      <circle class="node" cx="465" cy="175" r="6"/>
      <circle class="node" cx="239" cy="363" r="6"/>
      <circle class="node" cx="471" cy="363" r="6"/>
      <circle class="node" cx="359" cy="420" r="6"/>
    </g>

    <g class="service" text-anchor="middle">
      <rect class="label-box" x="50" y="124" width="154" height="18"/>
      <text class="service-label" x="127" y="137">ACCOUNT MANAGEMENT</text>
      <text class="service-item" x="127" y="157">Catalogue management</text>
      <text class="service-item" x="127" y="169">Account health monitoring</text>
      <text class="service-item" x="127" y="181">Case log &amp; issue resolution</text>
      <text class="service-item" x="127" y="193">Hub/Self-Ship Inventory</text>
      <text class="service-item" x="127" y="205">Management</text>
      <text class="service-item" x="127" y="217">Customised Reporting</text>
    </g>

    <g class="service" text-anchor="middle">
      <rect class="label-box" x="518" y="129" width="156" height="18"/>
      <text class="service-label" x="596" y="142">VENDORA ACCOUNT SETUP</text>
      <text class="service-item" x="596" y="163">Cost analysis to scale profitably</text>
      <text class="service-item" x="596" y="175">Vendora account setup</text>
      <text class="service-item" x="596" y="187">Account audit</text>
      <text class="service-item" x="596" y="199">Vendora Brand Registry</text>
    </g>

    <g class="service" text-anchor="middle">
      <rect class="label-box" x="38" y="381" width="155" height="18"/>
      <text class="service-label" x="115" y="394">VENDORA ADVERTISING</text>
      <text class="service-item" x="115" y="416">Sponsored Ads (PPC)</text>
      <text class="service-item" x="115" y="428">Bid automation</text>
      <text class="service-item" x="115" y="440">Demand-Side Platform (DSP)</text>
    </g>

    <g class="service" text-anchor="middle">
      <rect class="label-box" x="518" y="380" width="156" height="18"/>
      <text class="service-label" x="596" y="393">VENDORA ACCOUNT SETUP</text>
      <text class="service-item" x="596" y="413">Market opportunity analysis</text>
      <text class="service-item" x="596" y="425">Launch in new marketplaces</text>
      <text class="service-item" x="596" y="437">Listing localisation</text>
      <text class="service-item" x="596" y="449">Logistics &amp; Fulfilment strategy</text>
    </g>

    <g class="service" text-anchor="middle">
      <rect class="label-box" x="285" y="472" width="153" height="18"/>
      <text class="service-label" x="361" y="485">ACCOUNT MANAGEMENT</text>
      <text class="service-item" x="361" y="506">Catalogue management</text>
      <text class="service-item" x="361" y="518">Account health monitoring</text>
      <text class="service-item" x="361" y="530">Case log &amp; issue resolution</text>
      <text class="service-item" x="361" y="542">Hub/Self-Ship Inventory</text>
      <text class="service-item" x="361" y="554">Management</text>
      <text class="service-item" x="361" y="566">Customised Reporting</text>
    </g>
  </svg>

</main>
</body>
</html>
```